Brenton Wealth Management Flow Charts

I need help creating three flow charts for my businesses website. We want them to be simple but look professional. This is for a Wealth Management firm. I will attach a word document that has all of the descriptions for everything so you know what icons to use. We just want the chart to have an icon, the names of each step and the corresponding numbers. I will also include some examples of charts we liked as well. Once the winner is selected, we will need help with additional graphic design elements for our website ASAP.
- Goudy Roman

```html
<!DOCTYPE html>
<html lang="en">
<head>
<meta charset="utf-8">
<title>Brenton Wealth Management – Process Charts</title>
<link href="https://fonts.googleapis.com/css2?family=Sorts+Mill+Goudy&display=swap" rel="stylesheet">
<style>
  :root {
    --burgundy: #822f35;
    --gold: #c6a23d;
    --ink: #2b2b2b;
    --icon-tone: #e1e7f5;
    --paper: #ffffff;
  }
  * { box-sizing: border-box; margin: 0; padding: 0; }
  html, body { width: 1200px; height: 2209px; overflow: hidden; background: var(--paper); }
  body { position: relative; font-family: "Sorts Mill Goudy", Georgia, serif; color: var(--ink); }

  .chart { position: absolute; left: 0; width: 1200px; }
  .chart__top-bar { position: absolute; left: 40px; width: 1120px; height: 11px; top: 0; background: var(--burgundy); }
  .chart__bottom-band { position: absolute; left: 40px; width: 1120px; height: 39px; background: var(--burgundy); }
  .brand { position: absolute; right: 76px; font-size: 24px; letter-spacing: 2px; color: #3a3a3a; text-transform: uppercase; }
  .chart__title { position: absolute; left: 0; width: 1200px; text-align: center; font-size: 26px; font-weight: 400; color: var(--ink); }
  .chart__rule { position: absolute; left: 352px; width: 517px; height: 1px; background: var(--gold); }

  .steps { position: absolute; left: 0; width: 1200px; }
  .step { position: absolute; top: 0; transform: translateX(-50%); display: flex; flex-direction: column; align-items: center; text-align: center; white-space: nowrap; }
  .step__icon { width: 100px; height: 100px; border-radius: 14px; background: var(--icon-tone); }
  .step__bar { width: 53px; height: 6px; background: var(--burgundy); margin-top: 26px; }
  .step__num { margin-top: 12px; font-size: 11px; line-height: 14px; letter-spacing: 2px; color: var(--burgundy); text-transform: uppercase; font-weight: 700; }
  .step__label { margin-top: 6px; font-size: 22px; line-height: 30px; color: var(--gold); }
</style>
</head>
<body>

<section class="chart" style="top:49px">
  <div class="chart__top-bar"></div>
  <div class="brand" style="top:62px">Brenton</div>
  <h2 class="chart__title" style="top:182px">The Retirement Planning Process</h2>
  <div class="chart__rule" style="top:233px"></div>
  <div class="steps" style="top:306px">
    <div class="step" style="left:209px"><div class="step__icon" role="img" aria-label="Icon of an advisor meeting with clients at a table"></div><div class="step__bar"></div><div class="step__num">Step 1</div><div class="step__label">Discovery Meeting</div></div>
    <div class="step" style="left:410px"><div class="step__icon" role="img" aria-label="Icon of a client profile document"></div><div class="step__bar"></div><div class="step__num">Step 2</div><div class="step__label">Learning</div></div>
    <div class="step" style="left:610px"><div class="step__icon" role="img" aria-label="Icon of a financial checklist"></div><div class="step__bar"></div><div class="step__num">Step 3</div><div class="step__label">Planning</div></div>
    <div class="step" style="left:819px"><div class="step__icon" role="img" aria-label="Icon of a financial plan scroll"></div><div class="step__bar"></div><div class="step__num">Step 4</div><div class="step__label">Execution</div></div>
    <div class="step" style="left:1021px"><div class="step__icon" role="img" aria-label="Icon of three linked dollar gears"></div><div class="step__bar"></div><div class="step__num">Step 5</div><div class="step__label">Alignment</div></div>
  </div>
  <div class="chart__bottom-band" style="top:641px"></div>
</section>

<section class="chart" style="top:780px">
  <div class="chart__top-bar"></div>
  <div class="brand" style="top:62px">Brenton</div>
  <h2 class="chart__title" style="top:158px">Comprehensive Investment Management</h2>
  <div class="chart__rule" style="top:207px"></div>
  <div class="steps" style="top:292px">
    <div class="step" style="left:193px"><div class="step__icon" role="img" aria-label="Icon of a risk gauge"></div><div class="step__bar"></div><div class="step__num">1</div><div class="step__label">Understanding your<br>Risk Tolerance</div></div>
    <div class="step" style="left:393px"><div class="step__icon" role="img" aria-label="Icon of an investment report with a check mark"></div><div class="step__bar"></div><div class="step__num">2</div><div class="step__label">Investment<br>Selection</div></div>
    <div class="step" style="left:559px"><div class="step__icon" role="img" aria-label="Icon of an allocation wheel with a dollar sign"></div><div class="step__bar"></div><div class="step__num">3</div><div class="step__label">Asset<br>Allocation</div></div>
    <div class="step" style="left:704px"><div class="step__icon" role="img" aria-label="Icon of a tax form"></div><div class="step__bar"></div><div class="step__num">4</div><div class="step__label">Tax<br>Efficiency</div></div>
    <div class="step" style="left:868px"><div class="step__icon" role="img" aria-label="Icon of a calculator and growth chart"></div><div class="step__bar"></div><div class="step__num">5</div><div class="step__label">Distribution<br>Strategy</div></div>
    <div class="step" style="left:1051px"><div class="step__icon" role="img" aria-label="Icon of a strategy board on an easel"></div><div class="step__bar"></div><div class="step__num">6</div><div class="step__label">Behavior Finance<br>Coaching</div></div>
  </div>
  <div class="chart__bottom-band" style="top:641px"></div>
</section>

<section class="chart" style="top:1504px">
  <div class="chart__top-bar"></div>
  <div class="brand" style="top:62px">Brenton</div>
  <h2 class="chart__title" style="top:158px">Legacy and Estate Planning</h2>
  <div class="chart__rule" style="top:207px"></div>
  <div class="steps" style="top:292px">
    <div class="step" style="left:239px"><div class="step__icon" role="img" aria-label="Icon of a dollar sign linked to three beneficiaries"></div><div class="step__bar"></div><div class="step__num">1</div><div class="step__label">Beneficiaries</div></div>
    <div class="step" style="left:418px"><div class="step__icon" role="img" aria-label="Icon of a shield with a dollar sign"></div><div class="step__bar"></div><div class="step__num">2</div><div class="step__label">Trusts</div></div>
    <div class="step" style="left:601px"><div class="step__icon" role="img" aria-label="Icon of an estate document with a house"></div><div class="step__bar"></div><div class="step__num">3</div><div class="step__label">Estate Taxes<br>and Assessment</div></div>
    <div class="step" style="left:790px"><div class="step__icon" role="img" aria-label="Icon of a family home and a dollar wheel"></div><div class="step__bar"></div><div class="step__num">4</div><div class="step__label">Annual<br>Giving</div></div>
    <div class="step" style="left:992px"><div class="step__icon" role="img" aria-label="Icon of a hand giving a dollar coin"></div><div class="step__bar"></div><div class="step__num">5</div><div class="step__label">Donations<br>and Charity</div></div>
  </div>
  <div class="chart__bottom-band" style="top:642px"></div>
</section>

</body>
</html>
```